Website Design for Quarry Sun inc

I want eye candy on opening page.  Prefer yellows, greens and orange to darker colors.  This contest will be won on the home page, then we together will use that theme for the rest of the site (about 8 pages total, NO shopping cart).  My current site is www.BrindleRaySolar.com, you can use as much or as little of the content, photos, etc as you want.  I am Carl Dunmore - general partner.  The following web sites are ones that I like parts of, and would love an amalgm of them, based on my comments.  GOOD LUCK!

http://www.solarhaven.example/   -  The largest, most talked about company in the business, and a great site, probably my favorite.

 

 

http://www.tulmasolar.example/  -  Clean and clear

 

http://www.thebrightpowerhouse.example/index.html   -  Just for the pic of plug lit by sun

http://www.kestrel-solar.example/   -  Really like the general look of the site

 

http://www.solarloom.example/index.html  -  Good Flash sequence

 

http://www.dulasolar.example/cm/Home.html  -  Most offices in the business - not bad site

I don't know what a vector file is.  I have an AI file, does that work?  Meanwhile, I can't find how to upload it into my brief.  Advise.

Target Market(s)

NOT TREEHUGGERS!  Homeowners.  Retirees.  Early adopters.  OK, maybe a treehugger or two.  

Industry/Entity Type

Solar

Requirements
Must have
• Logo.  Any pics must be mine.  If you need more pics, email me.  Ease of use, compelling. 
Nice to have
• In California, Arizona and Nevada, and coming to a city near YOU!!

```html
<!DOCTYPE html>
<html lang="en">
<head>
<meta charset="utf-8">
<title>Quarry Sun inc — Home</title>
<link rel="stylesheet" href="https://fonts.googleapis.com/css2?family=Alegreya+Sans:wght@500;700&family=Varela+Round&family=Open+Sans:wght@600;700&display=swap">
<style>
:root{
  --sea:#0a8cc2;
  --sea-deep:#006f9f;
  --panel:#ebebed;
  --white:#ffffff;
  --link:#19a5de;
  --orange:#f7941d;
  --orange-light:#fdb84d;
  --sun-yellow:#e4ef00;
  --grey-text:#8a8a8a;
  --green:#5aad1e;
  --green-deep:#3f8f12;
  --green-bright:#4fae12;
  --dash:#7fd0f0;
}
*{box-sizing:border-box;margin:0;padding:0}
html,body{width:1200px;height:900px;overflow:hidden}
body{
  position:relative;
  background:radial-gradient(ellipse at 45% 55%, #0b9ed4 0%, var(--sea) 45%, var(--sea-deep) 100%);
  font-family:"Alegreya Sans",sans-serif;
}
.page-panel{
  position:absolute;left:247px;top:133px;width:676px;height:705px;
  background:var(--panel);
  border-radius:150px 70px 110px 210px / 170px 70px 110px 210px;
  box-shadow:0 2px 10px rgba(0,40,70,.25);
}
.logo-tab{
  position:absolute;left:225px;top:55px;width:183px;height:100px;
  background:var(--white);border-radius:26px;
  box-shadow:0 3px 8px rgba(0,40,70,.3);
  display:flex;align-items:center;justify-content:center;gap:8px;
}
.logo-dot{width:22px;height:22px;border-radius:50%;background:var(--orange)}
.logo-name{font-family:"Open Sans",sans-serif;font-weight:700;font-size:19px;color:#3c3c3c;line-height:1}

.main-nav{position:absolute;top:74px;left:440px;display:flex}
.main-nav a{
  display:flex;flex-direction:column;align-items:center;text-decoration:none;
  font-family:"Open Sans",sans-serif;font-weight:700;font-size:13px;letter-spacing:.3px;color:var(--white);
  position:absolute;
}
.main-nav svg{height:32px;margin-bottom:6px}
.main-nav .current{color:var(--sun-yellow)}

.office-burst{position:absolute;left:780px;top:66px;width:196px;height:196px}
.office-burst .offices{
  position:absolute;inset:0;display:flex;flex-direction:column;align-items:center;justify-content:center;
  color:var(--white);font-family:"Alegreya Sans",sans-serif;font-weight:700;font-size:13px;line-height:16px;text-align:center;
}
.offices .gap{height:15px}

.side-nav{position:absolute;left:293px;top:206px;width:176px}
.side-nav .why{
  display:block;height:29px;border-radius:4px;
  background:linear-gradient(var(--orange-light),var(--orange));
  color:var(--white);font-size:17px;padding:3px 0 0 8px;text-decoration:none;
  box-shadow:0 1px 2px rgba(0,0,0,.2);
}
.side-nav ul{list-style:none;margin-top:2px}
.side-nav li a{display:block;height:21.7px;padding-left:8px;color:var(--link);font-size:17px;text-decoration:none;line-height:21px}

.flash-box{
  position:absolute;left:282px;top:418px;width:193px;height:192px;border-radius:8px;
  background:linear-gradient(#8ec8ec 0%,#1a93d0 30%,#40a8dc 55%,#cfe6f4 100%);
  box-shadow:0 2px 4px rgba(0,0,0,.25);
  display:flex;justify-content:center;padding-top:34px;
}
.flash-box span{font-family:"Open Sans",sans-serif;font-weight:700;font-size:40px;color:var(--white);letter-spacing:-1px;height:48px}

.mail-icon{position:absolute;left:317px;top:624px;width:100px;height:76px}
.contact-email{position:absolute;left:283px;top:701px;font-size:17px;color:var(--link);text-decoration:none}

.column-rule{position:absolute;left:487px;top:165px;height:567px;border-left:1.5px dashed var(--dash)}

.photo{position:absolute;border:5px solid var(--orange);border-radius:18px;box-shadow:0 1px 3px rgba(0,0,0,.25)}
.photo-coast{left:500px;top:167px;width:109px;height:92px;background:linear-gradient(#4ba7d8,#3e7d4e 55%,#7a8c4c)}
.photo-villa{left:619px;top:167px;width:132px;height:92px;background:linear-gradient(#7fa280,#e6e6e6 45%,#4f7f3e)}
.photo-panels{left:501px;top:347px;width:126px;height:160px;border-radius:24px;background:linear-gradient(#9a8a80,#4b5580 40%,#2a3470)}

.tagline{
  position:absolute;left:499px;top:273px;width:399px;height:56px;border-radius:6px;
  background:linear-gradient(#fde0a8,var(--orange-light) 45%,var(--orange));
  box-shadow:0 2px 3px rgba(0,0,0,.2);
  padding:12px 0 0 10px;
  font-family:"Varela Round",sans-serif;font-size:15px;line-height:18px;color:var(--white);
  text-shadow:0 0 2px #b06000,0 1px 1px #a05000;
}

.benefits{position:absolute;left:635px;top:346px;width:265px;font-family:"Varela Round",sans-serif;color:var(--grey-text);font-size:11.5px}
.benefits p{position:absolute;white-space:nowrap}
.benefits b{color:var(--green-bright);font-weight:400;font-size:12px}
.tick{position:absolute;left:226px;width:36px;height:36px}

.about-box{
  position:absolute;left:498px;top:522px;width:403px;height:195px;border-radius:8px;
  background:linear-gradient(#86cc2c,var(--green) 55%,var(--green-deep));
  border:2px solid #3d8a10;
  padding:12px 12px 0 10px;
  font-family:"Open Sans",sans-serif;font-weight:600;font-size:6.4px;line-height:8.2px;color:var(--white);text-align:right;
}
.about-box p{margin-bottom:8px}
.about-box .dollar{position:absolute;left:8px;bottom:4px;font-family:"Open Sans",sans-serif;font-weight:700;font-size:44px;line-height:1;color:#7ed33a;text-shadow:0 1px 2px #2b6a08}

.footer-rule{position:absolute;left:283px;top:750px;width:601px;border-top:1.5px dashed var(--dash)}
.footer{position:absolute;left:298px;top:764px;font-family:"Varela Round",sans-serif;font-size:10px;color:var(--orange);white-space:nowrap}
.footer nav{display:inline;margin-left:16px}
.footer nav a{color:var(--orange);text-decoration:none}
</style>
</head>
<body>

<div class="page-panel"></div>

<header>
  <div class="logo-tab">
    <span class="logo-dot"></span>
    <span class="logo-name">Quarry Sun inc</span>
  </div>

  <nav class="main-nav">
    <a class="current" style="left:9px">
      <svg viewBox="0 0 40 32"><path d="M4 16 L20 3 L36 16 M9 13 V29 H31 V13" fill="none" stroke="currentColor" stroke-width="4" stroke-linejoin="round"/></svg>HOME</a>
    <a style="left:59px">
      <svg viewBox="0 0 40 32"><circle cx="26" cy="12" r="9" fill="none" stroke="currentColor" stroke-width="2.5"/><path d="M19 19 L6 31" stroke="currentColor" stroke-width="3"/></svg>RESOURCES</a>
    <a style="left:142px">
      <svg viewBox="0 0 40 32"><rect x="12" y="5" width="18" height="24" fill="none" stroke="currentColor" stroke-width="2"/><path d="M15 11h12M15 15h12M15 19h12M15 23h12" stroke="currentColor" stroke-width="1.5"/></svg>EMPLOYMENT</a>
    <a style="left:240px">
      <svg viewBox="0 0 44 32"><rect x="3" y="4" width="38" height="24" fill="none" stroke="currentColor" stroke-width="2.5"/><path d="M3 4 L22 18 L41 4 M3 28 L17 14 M41 28 L27 14" fill="none" stroke="currentColor" stroke-width="2.5"/></svg>CONTACT US</a>
  </nav>

  <div class="office-burst">
    <svg viewBox="0 0 200 200" width="196" height="196">
      <polygon fill="#f7941d" points="100,0 106,20 116,1 119,22 131,5 131,26 146,11 142,31 158,19 152,38 169,29 160,46 179,40 167,56 186,53 173,67 192,67 176,79 196,82 178,91 198,97 178,103 197,110 176,115 194,125 173,127 189,139 169,139 183,153 163,149 174,165 155,158 164,175 146,166 152,184 135,172 139,191 124,177 124,196 112,180 109,198 100,181 91,198 88,180 76,196 76,177 61,191 65,172 48,184 54,166 36,175 45,158 26,165 37,149 17,153 31,139 11,139 27,127 6,125 24,115 3,110 22,103 2,97 22,91 4,82 24,79 8,67 27,67 14,53 33,56 21,40 40,46 31,29 48,38 42,19 58,31 54,11 69,26 69,5 81,22 84,1 94,20"/>
      <circle cx="100" cy="100" r="66" fill="#fa8a1a" stroke="#ffb45a" stroke-width="4"/>
    </svg>
    <div class="offices">
      <span>FRESNO</span><span>(559) 555-0142</span>
      <span class="gap"></span>
      <span>SANTA BARBARA</span><span>(805) 555-0187</span>
    </div>
  </div>
</header>

<aside>
  <nav class="side-nav">
    <a class="why" href="#">Why Brindle Ray Solar?</a>
    <ul>
      <li><a href="#">Commercial Solar</a></li>
      <li><a href="#">Residential Solar</a></li>
      <li><a href="#">Products</a></li>
      <li><a href="#">Services</a></li>
      <li><a href="#">Project Gallery</a></li>
      <li><a href="#">Case Studies</a></li>
      <li><a href="#">FAQ</a></li>
      <li><a href="#">Company</a></li>
    </ul>
  </nav>

  <div class="flash-box" role="img" aria-label="Animated intro area: blue sky with white clouds"><span>FLASH</span></div>

  <svg class="mail-icon" viewBox="0 0 100 76">
    <polygon points="4,30 80,4 96,48 20,74" fill="#fafafa" stroke="#b9b9b9" stroke-width="1.5"/>
    <polyline points="4,30 52,44 80,4" fill="none" stroke="#c4c4c4" stroke-width="1.5"/>
    <path d="M60 46 H82 V39 L96 50 L82 61 V54 H60 Z" fill="#3fa62a"/>
  </svg>
  <a class="contact-email" href="#">info@brindleraysolar.com</a>
</aside>

<div class="column-rule"></div>

<main>
  <div class="photo photo-coast" role="img" aria-label="Photo of a hillside home with solar panels above the ocean"></div>
  <div class="photo photo-villa" role="img" aria-label="Photo of a white villa with rooftop solar panels"></div>

  <div class="tagline">Saving you money, while saving the planet since 1983<br>Go Solar Now!</div>

  <div class="photo photo-panels" role="img" aria-label="Close-up photo of a rooftop solar panel array"></div>

  <section class="benefits">
    <p style="left:0;top:0">Huge Government Rebates</p>
    <p style="left:7px;top:16px">Up to <b>25%</b> residential</p>
    <p style="left:7px;top:32px">Up to <b>90%</b> commercial</p>
    <p style="left:7px;top:66px">Lower or Eliminate your Electric Bill</p>
    <p style="left:7px;top:99px">No More Rate Hikes...Ever</p>
    <p style="left:7px;top:142px">Our Systems Pay for Themselves from Day One!</p>
    <svg class="tick" style="top:2px" viewBox="0 0 36 36"><circle cx="18" cy="18" r="17" fill="#4ea91a" stroke="#2f7a0c"/><path d="M9 18 L15 24 L27 11" fill="none" stroke="#fff" stroke-width="5" stroke-linecap="round"/></svg>
    <svg class="tick" style="top:46px" viewBox="0 0 36 36"><circle cx="18" cy="18" r="17" fill="#4ea91a" stroke="#2f7a0c"/><path d="M9 18 L15 24 L27 11" fill="none" stroke="#fff" stroke-width="5" stroke-linecap="round"/></svg>
    <svg class="tick" style="top:89px" viewBox="0 0 36 36"><circle cx="18" cy="18" r="17" fill="#4ea91a" stroke="#2f7a0c"/><path d="M9 18 L15 24 L27 11" fill="none" stroke="#fff" stroke-width="5" stroke-linecap="round"/></svg>
  </section>

  <section class="about-box">
    <p>You hear it on TV, Radio, Print and the Web. Everyone is bragging about their new ‘Going Green’ policy. It’s the latest craze, and there are a lot of big corporations as well as fly-by-nights operations that are capitalizing on the trend.</p>
    <p>We installed our first solar system back in 1983, and have been leaders in energy conservation and developing new technologies ever since. We’ve experienced living completely off-grid using only solar panels and a wind generator. Our solar panel installations have made hundreds of homes more energy efficient.</p>
    <p>Not too many people understand that your contribution to protecting the world starts at home. Solar energy is one of the most efficient ways of saving energy, the environment and money. The United States accounts for only 5 percent of the world’s population, yet we consume 26 percent of the world’s energy. We need to make a change and going solar is where it begins.</p>
    <p>Brindle Ray Solar helps you identify your energy spending trends and creates a green solution by building the best solar system from top-quality equipment. We help you save money, and the earth.</p>
    <p>Browse our website to learn about the benefits of solar power for your business or home and contact us in Santa Barbara or Fresno today to receive a free rate quote.</p>
    <p>*If your electric bill is over $150 mo.</p>
    <span class="dollar">$</span>
  </section>
</main>

<div class="footer-rule"></div>
<footer class="footer">
  Copyright 2008 Brindle Ray Solar, Fresno, CA. All rights reserved.
  <nav><a href="#">Home</a> | <a href="#">Company</a> | <a href="#">Services</a> | <a href="#">FAQ</a> | <a href="#">Contact Us</a> | <a href="#">Sitemap</a></nav>
</footer>

</body>
</html>
```